Economics and Investing for women with a humorous narrative

I need a logo and business card design for my company:
The Velvet Almanac LLC. TVA is an educational website dedicated to translating the language of economics and investing into concepts that are interesting, easy to understand and funny.
As the target market is for women, the card needs to be NON traditional in terms of finance and investing. No pictures of charts, currencies, stock markets etc. This needs to be colorful , inviting and memorable.
The driver of the site is to present difficult concepts with a humorous tilt. If Gregory Tandy (A Paper Orchard) collaborated with Lila Brandt what would it look like?

Reason: I don't think I did a good enough job of explaining what I was looking for including the type of color palette. I asked that the cards NOT look so corporate. I have updated my brief and included 3 pictures of a color scheme I like along with design. I also update the information to be included on the card.

Target Market(s)

Women 30-50

Industry/Entity Type

Business

Contact Information for Business Card

The Velvet Almanac LLC
Dana Holloway , CEO
482 Wexley Street
Suite 2300
New York, New York 10017

Phone: 212-555-0143
TheVelvetAlmanac.com
Email: dana@thevelvetalmanac.com

Font styles to use
Other font styles liked:
• LustPro Demi No.3

Requirements
Must have
• Gravitas, bold warm colors, the antithesis of modest
Nice to have
• Isn't this why I am hiring designers?
Should not have
• Charts, graphs, numbers, currency, stock or bond market pictures, any reference to investing . Do not want this to look like a boring investment business card

```html
<!DOCTYPE html>
<html lang="en">
<head>
<meta charset="utf-8">
<title>The Velvet Almanac LLC — Business Card</title>
<link rel="stylesheet" href="https://fonts.googleapis.com/css2?family=Source+Sans+3:wght@400;600&display=swap">
<style>
  :root {
    --backdrop: #87875f;
    --card-front: #c4553c;
    --card-front-edge: #a94430;
    --card-cream: #f9eec8;
    --card-cream-edge: #eadfb6;
    --stitch-front: #f3cbb9;
    --stitch-cream: #d9cfa8;
    --ink-cream: #fbf0d2;
    --ink-warm: #b4503a;
    --name-faint: #e6d9b4;
    --branch-front-a: rgba(226, 120, 92, 0.6);
    --branch-front-b: rgba(196, 85, 60, 0);
    --branch-cream-a: rgba(225, 210, 170, 0.75);
    --branch-cream-b: rgba(249, 238, 200, 0);
  }
  html, body {
    margin: 0;
    width: 1200px;
    height: 900px;
    overflow: hidden;
    background: var(--backdrop);
    font-family: "Source Sans 3", "Myriad Pro", sans-serif;
  }
  .card {
    position: absolute;
    left: 384px;
    width: 404px;
    height: 243px;
    border-radius: 12px;
    box-sizing: border-box;
  }
  .card__stitch {
    position: absolute;
    inset: 6px;
    border-radius: 9px;
    border: 1px dashed var(--stitch-front);
  }
  .card--front {
    top: 183px;
    background: var(--card-front);
    border: 3px solid var(--card-front-edge);
  }
  .card--back {
    top: 474px;
    background: var(--card-cream);
    border: 2px solid var(--card-cream-edge);
  }
  .card--back .card__stitch { border-color: var(--stitch-cream); }

  .wordmark {
    position: absolute;
    left: 24px;
    top: 54px;
    margin: 0;
    color: var(--ink-cream);
    font-weight: 400;
    font-size: 22px;
    line-height: 1.05;
  }
  .wordmark__dot {
    display: block;
    width: 14px;
    height: 14px;
    border-radius: 50%;
    background: var(--ink-cream);
    margin: 0 0 6px 2px;
  }
  .wordmark__line { display: block; }
  .wordmark__sub { font-size: 15px; padding-left: 30px; margin-top: 1px; }

  .branch {
    position: absolute;
    border-radius: 50% 0 0 0;
  }
  .card--front .branch {
    left: 232px; top: 70px; width: 162px; height: 160px;
    background: radial-gradient(ellipse at 80% 55%, var(--branch-front-a), var(--branch-front-b) 70%);
  }
  .card--back .branch {
    left: 232px; top: 76px; width: 164px; height: 156px;
    background: radial-gradient(ellipse at 75% 55%, var(--branch-cream-a), var(--branch-cream-b) 70%);
  }

  .back-name {
    position: absolute;
    left: 0;
    right: 0;
    top: 44px;
    margin: 0;
    text-align: center;
    color: var(--name-faint);
    font-weight: 400;
    font-size: 22px;
  }

  .contact {
    position: absolute;
    left: 25px;
    top: 134px;
    color: var(--ink-warm);
    font-size: 7.6px;
    line-height: 10.6px;
  }
  .contact__name {
    font-size: 12px;
    line-height: 14px;
    margin: 0 0 2px;
    font-weight: 400;
  }
  .contact p { margin: 0; }
</style>
</head>
<body>
  <section class="card card--front" aria-label="Business card front">
    <div class="card__stitch"></div>
    <h1 class="wordmark">
      <span class="wordmark__dot" aria-hidden="true"></span>
      <span class="wordmark__line">THE VELVET</span>
      <span class="wordmark__line wordmark__sub">Almanac LLC</span>
    </h1>
    <div class="branch" role="img" aria-label="Faint line illustration of a flowering branch with buds and leaves"></div>
  </section>

  <section class="card card--back" aria-label="Business card back">
    <div class="card__stitch"></div>
    <p class="back-name">The Velvet Almanac</p>
    <div class="contact">
      <h2 class="contact__name">Dana Holloway , CEO</h2>
      <p>482 Wexley Street</p>
      <p>Suite 2300</p>
      <p>New York, New York 10017</p>
      <p>Phone: 212-555-0143</p>
      <p>TheVelvetAlmanac.com</p>
      <p>Email: dana@thevelvetalmanac.com</p>
    </div>
    <div class="branch" role="img" aria-label="Line illustration of a flowering branch with buds and leaves"></div>
  </section>
</body>
</html>
```